A website design for a consultation firm

We are located in Istanbul, Turkey and offers our consultation services to customers interested in investing in Realestate, Education and Investment particularly this coming from Arab world and English speaking countries.

The site should carry our message of deep knowledge about the Turkish markets in the mentioned sectors of interest, sincerity and keenness.

The final deliverable of the winning design should include:
- The source files of the final designs. e.g. AI, PSD ..etc
- The redline markup for the design using a Specctr or any other similar tool.

Target Market(s)

English and Arabic speaking countries with a Turkish theme since we are a Turkish company

Industry/Entity Type

Consulting

Number of Pages Required

2 page

Font styles to use
Sans Serif

Requirements
Must have
• The site should serve the following main sections:
• - Why QVE?
• - Reports & studies
• - Sectors
• - Our team
• - Contact
• We need a design that could be converted into a WordPress theme.
• The design should be in English but should accommodate other languages including RTL.
• You can use the color theme you like as long as it does't dissolve the logo.
• The site should link into our accounts on the following networks:
• - Twitter
• - Facebook
• - LinkedIn
• The design should be responsive and nicely rendered on Desktop, Tablets and Smart phones.
Nice to have
• The site would be nice to balance between being informative and

```html
<!DOCTYPE html>
<html lang="en">
<head>
<meta charset="utf-8">
<title>QVE Consulting</title>
<link rel="stylesheet" href="https://fonts.googleapis.com/css2?family=Fira+Sans:wght@400;500;600&display=swap">
<style>
  :root {
    --red: #e3141f;
    --navy: #1f3566;
    --ink: #1d1d1d;
    --body: #555555;
    --muted: #6c6c6c;
    --light: #f2f2f2;
    --frame: #ebebeb;
    --button: #e2e2e2;
    --orange: #f5a800;
    --white: #ffffff;
  }
  * { box-sizing: border-box; margin: 0; padding: 0; }
  html, body { width: 863px; height: 1200px; overflow: hidden; }
  body { position: relative; font-family: "Fira Sans", Arial, sans-serif; color: var(--ink); background: var(--white); }
  .abs { position: absolute; }

  .hero { left: 0; top: 0; width: 863px; height: 498px;
    background: linear-gradient(100deg, #d9cbb6 0%, #e8b03a 22%, #3a5f8f 42%, #e9e4dc 58%, #b07048 75%, #6d6d72 100%); }
  .brand { left: 53px; top: 30px; display: flex; align-items: center; gap: 8px;
    font-size: 26px; font-weight: 600; color: var(--navy); }
  .brand-dot { width: 14px; height: 14px; border-radius: 50%; background: var(--red); }
  .hotline { left: 620px; top: 16px; display: flex; gap: 8px; align-items: center; }
  .hotline-label { font-size: 11px; color: var(--ink); line-height: 1.2; }
  .hotline-number { font-size: 12.5px; color: var(--red); font-weight: 500; }
  .lang { left: 756px; top: 17px; width: 54px; height: 23px; background: rgba(255,255,255,.85);
    border-radius: 2px; font-size: 10px; color: var(--muted); display: flex; align-items: center; justify-content: center; gap: 3px; }
  .nav { left: 383px; top: 60px; display: flex; gap: 23px; font-size: 11px; color: var(--ink); list-style: none; }

  .why { left: 53px; top: 531px; width: 369px; height: 203px; background: var(--frame); padding: 6px; }
  .why-inner { background: var(--white); width: 100%; height: 100%; padding: 22px 20px; }
  .why h2 { font-size: 16px; font-weight: 500; color: var(--red); }
  .why h3 { font-size: 12px; font-weight: 500; margin-top: 6px; }
  .why p { font-size: 9.6px; line-height: 16px; color: var(--body); margin-top: 11px; }
  .btn { display: inline-block; background: var(--button); color: #555; font-size: 9.5px;
    padding: 6px 8px; border-radius: 2px; }
  .why .btn { margin-top: 15px; }

  .sector { top: 531px; width: 175px; height: 203px; }
  .sector-photo { height: 134px; }
  .sector-band { height: 69px; color: var(--white); text-align: center; padding-top: 16px; }
  .sector-band h4 { font-size: 11.5px; font-weight: 500; letter-spacing: .2px; }
  .sector-band span { display: block; font-size: 9px; margin-top: 10px; }
  .real { left: 442px; }
  .real .sector-photo { background: linear-gradient(180deg, #8fb8e0 0%, #e6e0d4 45%, #3f6b3a 80%, #2c4f6a 100%); }
  .real .sector-band { background: var(--navy); }
  .edu { left: 635px; }
  .edu .sector-photo { background: linear-gradient(135deg, #f2ece6 0%, #e8b6a8 50%, #9fc3e0 100%); }
  .edu .sector-band { background: var(--red); }

  .reports-title { left: 53px; top: 763px; font-size: 14.5px; font-weight: 500; }
  .report-photo { left: 53px; top: 797px; width: 175px; height: 120px;
    background: linear-gradient(180deg, #c9a77a 0%, #9a7a5c 40%, #6c5646 70%, #4a3e3a 100%); }
  .report { left: 247px; top: 794px; width: 300px; }
  .report h3 { font-size: 12px; font-weight: 500; }
  .report .lead { font-size: 9.6px; color: var(--body); margin-top: 5px; }
  .report p { font-size: 9.6px; line-height: 16px; color: var(--body); margin-top: 12px; }
  .report .btn { margin-top: 12px; }
  .team { left: 571px; top: 767px; width: 239px; height: 150px;
    background: linear-gradient(160deg, #b9c0c8 0%, #7d8894 50%, #3a4654 100%); }
  .team-label { position: absolute; left: 0; right: 0; bottom: 22px; height: 19px;
    background: rgba(255,255,255,.82); font-size: 10.5px; font-weight: 500; text-align: center; line-height: 19px; }

  .connect { left: 0; top: 950px; width: 863px; height: 66px; background: var(--light);
    border-top: 1px solid #e4e4e4; border-bottom: 1px solid #e4e4e4; }
  .connect h2 { position: absolute; left: 143px; top: 24px; font-size: 14.5px; font-weight: 500; }
  .connect p { position: absolute; left: 333px; top: 19px; width: 270px; font-size: 9.6px; line-height: 13px; color: var(--body); }
  .signup { position: absolute; left: 635px; top: 19px; width: 83px; height: 28px; border-radius: 14px;
    background: var(--orange); color: var(--white); font-size: 11px; font-weight: 600;
    display: flex; align-items: center; justify-content: center; gap: 6px; }

  .footer { left: 0; top: 1016px; width: 863px; height: 148px; background: var(--light); }
  .map { left: 53px; top: 1034px; width: 110px; height: 80px; background: linear-gradient(135deg, #e6e3dc, #d7dde3); }
  .fcol { top: 1047px; font-size: 9.6px; color: var(--body); line-height: 16px; }
  .fcol h4 { font-size: 10.5px; font-weight: 500; color: var(--ink); margin-bottom: 4px; }
  .fcol ul { list-style: none; }
  .foot-brand { left: 706px; top: 1072px; font-size: 22px; font-weight: 600; color: var(--navy); display: flex; align-items: center; gap: 7px; }
  .copyright { left: 0; top: 1175px; width: 863px; text-align: center; font-size: 9.6px; color: var(--body); }
</style>
</head>
<body>

<header>
  <div class="hero abs" role="img" aria-label="Photo of a smiling couple reviewing house plans with a consultant holding a small model house"></div>
  <div class="brand abs"><span class="brand-dot"></span>QVE Consulting</div>
  <div class="hotline abs">
    <svg width="18" height="22" viewBox="0 0 18 22" aria-hidden="true"><circle cx="9" cy="6" r="5" fill="#1d1d1d"/><path d="M1 22c0-6 3.5-9 8-9s8 3 8 9z" fill="#1d1d1d"/></svg>
    <div><div class="hotline-label">Free Consulation</div><div class="hotline-number">(800) 555 0142</div></div>
  </div>
  <div class="lang abs">English <svg width="5" height="4" viewBox="0 0 5 4"><path d="M0 0h5L2.5 4z" fill="#999"/></svg></div>
  <ul class="nav abs">
    <li>Home</li><li>About Us</li><li>Services</li><li>Report &amp; Studies</li><li>Testimonials</li><li>Contact Us</li>
  </ul>
</header>

<main>
  <section class="why abs">
    <div class="why-inner">
      <h2>Why QVE?</h2>
      <h3>Mission: unlock the Turkish market for investors</h3>
      <p>Lorem Ipsum is simply dummy text of the printing and typesetting industry. Lorem Ipsum has been the industry's standard dummy text ever since the 1500s, when an unknown printer took a galley of type and scrambled it to make a type specimen book.</p>
      <span class="btn">LEARN MORE</span>
    </div>
  </section>

  <article class="sector real abs">
    <div class="sector-photo" role="img" aria-label="Photo of a white villa with red roofs among palm trees"></div>
    <div class="sector-band"><h4>REALESTATE INVESTMENT</h4><span>LEARN MORE ⊙</span></div>
  </article>
  <article class="sector edu abs">
    <div class="sector-photo" role="img" aria-label="Photo of a mother and child saving coins in a pink piggy bank"></div>
    <div class="sector-band"><h4>EDUCATION INVESTMENT</h4><span>LEARN MORE ⊙</span></div>
  </article>

  <h2 class="reports-title abs">Reports &amp; Studies</h2>
  <div class="report-photo abs" role="img" aria-label="Photo of an Istanbul hillside cityscape by the water at dusk"></div>
  <article class="report abs">
    <h3>The Realestate smart investor guide</h3>
    <div class="lead">Looking to minimize the new market entrance risk?</div>
    <p>Lorem Ipsum is simply dummy text of the printing and typesetting industry. Lorem Ipsum has been the industry's standard dummy text and scrambled it to make a type specimen book.</p>
    <span class="btn">LEARN MORE</span>
  </article>
  <div class="team abs" role="img" aria-label="Photo of a smiling business team in an office">
    <div class="team-label">OUR TEAM MEMBERS ⊙</div>
  </div>

  <section class="connect abs">
    <h2>Let’s Stay Connected!</h2>
    <p>Sign up today for our newsletter and receive latest news and also get our tips &amp; exclusive offers.</p>
    <div class="signup">SIGN UP
      <svg width="15" height="15" viewBox="0 0 15 15" aria-hidden="true"><circle cx="7.5" cy="7.5" r="7.5" fill="#fff"/><path d="M6 4l3.5 3.5L6 11" stroke="#f5a800" stroke-width="1.6" fill="none"/></svg>
    </div>
  </section>
</main>

<footer>
  <div class="footer abs"></div>
  <svg class="abs" style="left:420px;top:1010px" width="24" height="12" viewBox="0 0 24 12" aria-hidden="true">
    <path d="M0 6h6M18 6h6" stroke="#f5a800" stroke-width="2"/><rect x="6" y="1" width="9" height="10" rx="2" fill="#f5a800"/><path d="M15 3h4M15 9h4" stroke="#f5a800" stroke-width="2"/>
  </svg>
  <div class="map abs" role="img" aria-label="Street map showing the office location with a red pin"></div>
  <div class="fcol abs" style="left:182px">
    <h4>QVE Consulting</h4>
    228, Loremipsum dolor sit,<br>dsosisk amet 854987<br><br>
    T: (800) 555 0142<br>E: info@qveconsulting.com
  </div>
  <div class="fcol abs" style="left:377px">
    <h4>Quick Links</h4>
    <ul><li>Home</li><li>About Us</li><li>Services</li></ul>
  </div>
  <div class="fcol abs" style="left:458px;top:1067px">
    <ul><li>Report &amp; Studies</li><li>Testimonials</li><li>Contact Us</li></ul>
  </div>
  <div class="fcol abs" style="left:590px">
    <h4>Information</h4>
    <ul><li>Terms of Use</li><li>Privacy Policy</li><li>SItemap</li></ul>
  </div>
  <div class="foot-brand abs"><span class="brand-dot"></span>QVE</div>
  <div class="copyright abs">© 2016 QVE Consulting. All Rights Reserved</div>
</footer>

</body>
</html>
```